Expanding Software Company Needs a Wordpress Design Project

Our software company is expanding, and we are looking for a fantastic Wordpress designer that we can work with on this small project to start, and ideally develop a relationship with over time. This initial project will require the designer to either identify and customize an existing Wordpress Theme or to create a new WP Theme from scratch.
What we are looking for in a WP Theme needs to be modern, creative, professional, and colorful. The Template also needs to be scalable and able to grow with our business. We have many related businesses primarily in the field of home-repair and we would like to be able to use this same template framework for our other businesses, but be able to change / modify the color scheme and some of the basic features like images, fonts, and navigation buttons titles. Ultimately, we want people to be able to go from one of our websites to another and not feel like it is the same website and cause confusion for the end-user.

Please submit an example home page and inside page for each of the following types of businesses (so we can see how the design can vary from site to site):
- Window Washing
- Painting
- Plumbing
Updates

Project Deadline Extended
Reason: Deadline Extended due to Holiday in the United States. Thank you.

Industry/Entity Type

Software

Requirements
Must have
• 1. We are looking for a standard Five Page design with Spectacular Home Page, About Us, Services, Gallery, and Contact Us pages, though we need to have some flexibility in the main menu/sub-menu options as we grow.
2. Need the ability to modify throughout with different color schemes, fonts, and images.
3. The navigation buttons must be visible on each page, but does not have to be “at the top”…. It can be wherever your design allows….but must be consistent on every page.
4. The Home Landing Page needs to be exciting and attractive to the eye. The other, inside pages can be less so, but still needs to be more than just text.
5. We would like to have testimonial and FAQ pages as optional plugins for scalability.
6. The Contact Us page needs to have a customizable form that could be a simple contact form, or could be for requesting a free-quote.
7. Need the ability to integrate with a newsletter / mailing list.
8. We’ll need links and sharing buttons for social media available as options as well, though do not always want them visible on the site.
9. The site needs to be user friendly and easy to navigate.
Nice to have
• Example: An example of a website/theme we like is: http://brightlacquerworks.example

```html
<!DOCTYPE html>
<html lang="en">
<head>
<meta charset="utf-8">
<title>Verano – Painting, Window Washing &amp; Plumbing</title>
<link href="https://fonts.googleapis.com/css2?family=Ubuntu:wght@300;400;500;700&family=Arimo:wght@400;700&display=swap" rel="stylesheet">
<style>
:root{
  --green-dark:#1f8a0c;
  --green:#3aad12;
  --green-light:#5cc41f;
  --green-pale:#c9f2a6;
  --red:#b5302c;
  --blue:#2a84c6;
  --orange:#ef9a1c;
  --text:#555;
  --grey-bg:#e6e6e3;
  --footer:#3b3b3b;
  --white:#fff;
}
*{margin:0;padding:0;box-sizing:border-box}
html,body{width:1015px;height:1200px;overflow:hidden}
body{position:relative;background:var(--grey-bg);font-family:"Arimo",Arial,sans-serif;color:var(--text)}
.abs{position:absolute}
.top-band{left:0;top:0;width:1015px;height:134px;background:linear-gradient(#3ea219,#2c9512 60%,#24870c)}
.logo{left:76px;top:10px;font-family:"Ubuntu",sans-serif;font-weight:700;font-size:50px;color:var(--white);letter-spacing:-1px}
.swatches{left:612px;top:28px;display:flex;gap:4px}
.swatches span{width:25px;height:25px;border:2px solid var(--white)}
.font-size{left:703px;top:28px;display:flex;gap:4px}
.font-size span{width:24px;height:24px;border:1px solid #6cc54a;color:#cfeebd;font-family:"Ubuntu",sans-serif;display:flex;align-items:center;justify-content:center}
.search{left:796px;top:28px;width:143px;height:24px;background:var(--white);border:1px solid #ddd;font-size:10px;color:#333;padding:6px 10px}
.search svg{position:absolute;right:8px;top:5px}
.page{left:76px;top:90px;width:864px;height:934px;background:var(--white)}
.nav{left:84px;top:98px;display:flex;font-family:"Ubuntu",sans-serif;font-size:13px;color:#333}
.nav a{color:inherit;text-decoration:none;height:36px;line-height:36px;padding:0 15px;margin-right:13px}
.nav a.active{background:#eee;color:var(--green-dark);border-radius:4px 4px 0 0}
.call{left:750px;top:104px;font-family:"Ubuntu",sans-serif;font-size:15px;color:var(--red)}
.nav-rule{left:83px;top:134px;width:849px;height:3px;background:var(--green)}
.slider-frame{left:83px;top:137px;width:849px;height:292px;background:#e8e8e6}
.slider{left:90px;top:146px;width:835px;height:275px;background:linear-gradient(110deg,#138f07,#3cb613 55%,#4fc21a)}
.slider h1{position:absolute;left:47px;top:45px;font-family:"Ubuntu",sans-serif;font-weight:700;font-size:24px;color:var(--white)}
.slider p{position:absolute;left:47px;top:80px;width:340px;font-family:"Ubuntu",sans-serif;font-weight:300;font-size:21px;line-height:27px;color:var(--green-pale)}
.slider .more{position:absolute;left:47px;top:149px;width:84px;height:27px;background:#f2f2f2;border-radius:3px;font-family:"Ubuntu",sans-serif;font-size:11px;color:#555;display:flex;align-items:center;justify-content:center}
.dots{position:absolute;left:24px;top:235px;display:flex;gap:6px}
.dots span{width:12px;height:12px;border-radius:50%;background:#f0f0f0}
.dots span:first-child{background:var(--green);border:2px solid #f0f0f0}
.slider-photo{position:absolute;right:0;top:0;width:300px;height:275px;background:linear-gradient(100deg,rgba(255,255,255,0) 0,#f4f4f0 18%,#e8e3da 70%,#d8d1c6)}
h2{font-family:"Ubuntu",sans-serif;font-weight:400;font-size:20px;color:var(--red)}
.para{font-size:11.5px;line-height:19.5px;color:#555;text-align:justify}
.welcome{left:85px;top:448px;width:597px}
.welcome h2{margin-bottom:8px}
.welcome .para+.para{margin-top:7px}
.video{left:699px;top:486px;width:233px;height:131px;background:#dcdcda;padding:7px}
.video .shot{width:100%;height:100%;background:linear-gradient(120deg,#c9c2b8,#c9848a 55%,#b8aea4);position:relative}
.video svg{position:absolute;left:99px;top:40px}
.divider{left:85px;top:642px;width:847px;height:1px;background:#e0e0e0}
.services{left:85px;top:657px;width:597px}
.services h2{margin-bottom:8px}
.card{top:759px;width:194px;height:145px;border-radius:4px;padding:4px;font-family:"Ubuntu",sans-serif;font-size:14px;color:var(--white)}
.card .pic{height:109px;border-radius:3px}
.card .label{text-align:center;margin-top:11px}
.card.blue{left:84px;background:var(--blue)}
.card.blue .pic{background:linear-gradient(#fff 40%,#e7e2dc)}
.card.green{left:286px;background:#149e0c}
.card.green .pic{background:linear-gradient(135deg,#c7d896,#7fa64a 60%,#a8c071)}
.card.orange{left:488px;background:var(--orange)}
.card.orange .pic{background:linear-gradient(160deg,#6f8aa4,#4e6b87)}
.testi-head{left:699px;top:657px;width:233px}
.testi-head svg{position:absolute;right:0;top:8px}
.testi{left:699px;top:695px;width:233px;height:208px;background:var(--red);border-radius:4px}
.testi .bubble{position:absolute;left:7px;top:7px;width:219px;height:165px;background:var(--white);border-radius:3px;padding:12px 18px;font-size:11.5px;line-height:19.5px;font-style:italic;color:#777;text-align:justify}
.testi .quote{font-family:Georgia,serif;font-style:normal;font-weight:700;font-size:18px;color:#999;line-height:10px}
.testi .name{position:absolute;left:22px;top:183px;font-family:"Ubuntu",sans-serif;font-weight:500;font-size:11.5px;color:var(--white)}
.testi .tail{position:absolute;left:190px;top:171px}
.faq{left:83px;top:919px;width:849px;height:100px;background:linear-gradient(#fff,#f0f0ee);border:1px solid #e2e2e0;border-radius:4px}
.faq .badge{position:absolute;left:0;top:8px;width:86px;height:82px;border-right:1px solid #ddd;text-align:center}
.faq .badge b{display:block;font-family:"Ubuntu",sans-serif;font-weight:500;font-size:20px;color:var(--red);margin-top:6px}
.faq h3{position:absolute;left:104px;top:24px;font-size:13px;color:#333}
.faq p{position:absolute;left:104px;top:50px;width:680px;font-size:12px;line-height:18px;color:#666}
.faq .next{position:absolute;right:18px;top:38px}
.links{top:1033px;list-style:none;font-size:11.5px;color:#555}
.links li{height:25px}
.links li::before{content:"• ";color:#888}
.col-rule{left:686px;top:1040px;width:1px;height:92px;background:#ccc}
.signup{left:718px;top:1038px}
.signup h4{font-family:"Ubuntu",sans-serif;font-weight:400;font-size:16px;color:var(--green-dark)}
.signup .field{position:absolute;left:0;top:27px;width:217px;height:29px;background:var(--white);border:1px solid #ccc;font-size:10px;color:#666;padding:9px 14px;white-space:nowrap}
.signup .submit{position:absolute;left:157px;top:63px;width:60px;height:23px;background:linear-gradient(#8a8a8a,#5d5d5d);color:var(--white);font-size:12px;font-weight:700;display:flex;align-items:center;justify-content:center}
.footer{left:0;top:1147px;width:1015px;height:53px;background:var(--footer)}
.footer p{position:absolute;left:76px;top:19px;font-size:12px;font-weight:700;color:#cfcfcf;word-spacing:2px}
.social{position:absolute;left:849px;top:15px;display:flex;gap:11px}
.social span{width:22px;height:22px;border-radius:50%;border:2px solid #eee}
</style>
</head>
<body>
<div class="abs top-band"></div>
<div class="abs logo">Verano</div>
<div class="abs swatches"><span style="background:#2f9a12"></span><span style="background:#1f7fc4"></span><span style="background:#ef9a1c"></span></div>
<div class="abs font-size"><span style="font-size:10px">A</span><span style="font-size:13px;color:#fff">A</span><span style="font-size:17px">A</span></div>
<div class="abs search">Search
  <svg width="14" height="14" viewBox="0 0 14 14"><circle cx="5.5" cy="5.5" r="4" fill="none" stroke="#222" stroke-width="2"/><line x1="8.5" y1="8.5" x2="13" y2="13" stroke="#222" stroke-width="2.5"/></svg>
</div>

<div class="abs page"></div>
<nav class="abs nav"><a class="active" href="#">Home</a><a href="#">About Us</a><a href="#">Services</a><a href="#">Gallery</a><a href="#">Contact Us</a></nav>
<div class="abs call">
  <svg width="16" height="14" viewBox="0 0 16 14" style="vertical-align:-2px"><path d="M3 1 L6 4 L4.5 6 Q6.5 9 9.5 10 L11 8.5 L14 11.5 L12 13.5 Q5 12 1.5 3 Z" fill="#b5302c"/></svg>
  Call us : 555 014 2290</div>
<div class="abs nav-rule"></div>

<div class="abs slider-frame"></div>
<section class="abs slider">
  <h1>We are into painting business</h1>
  <p>Other services we do are Window Washing &amp; Plumbing.</p>
  <div class="more">VIEW MORE</div>
  <div class="dots"><span></span><span></span><span></span><span></span></div>
  <div class="slider-photo" role="img" aria-label="Painter raising a brush against a freshly painted white wall"></div>
</section>

<section class="abs welcome">
  <h2>Welcome to Verano</h2>
  <p class="para">Phasellus volutpat tincidunt eros, quis tristique nunc condimentum at. Duis tristique justo in dui tristique auctor tristique ligula rutrum. Quisque bibendum sodales lorem, id varius nunc vehicula sit amet. Sed dictum, purus dignissim imperdiet blandit, dui metus ultricies est, ac tincidunt felis tellus vitae leo. Vestibulum ornare diam a leo vehicula auctor. In lobortis est et libero feugiat iaculis rhoncus eros ullamcorper. Aenean luctus porttitor sem, a laoreet mi dictum eu. Proin at odio lacus, id dictum lectus. Vestibulum placerat quam non lectus suscipit vel aliquet elit accumsan.</p>
  <p class="para">Curabitur mattis mauris ac leo interdum commodo. Curabitur vitae dolor libero. Vivamus feugiat vehicula risus, ut sollicitudin lectus suscipit eu. In fringilla dapibus ipsum vitae volutpat.</p>
</section>
<div class="abs video">
  <div class="shot" role="img" aria-label="Video still of a painter rolling red paint onto a wall">
    <svg width="38" height="38" viewBox="0 0 38 38"><circle cx="19" cy="19" r="18" fill="#eee" stroke="#999"/><path d="M15 12 L26 19 L15 26 Z" fill="#444"/></svg>
  </div>
</div>

<div class="abs divider"></div>

<section class="abs services">
  <h2>Our Services</h2>
  <p class="para">Donec interdum, ipsum id sodales tempor, mi turpis molestie arcu, tincidunt placerat ipsum tortor sit amet dolor. Cras auctor velit vestibulum tellus vehicula varius. Nam tincidunt eros a libero fermentum lacinia. Fusce id lorem in nibh bibendum blandit non at mi.</p>
</section>
<div class="abs card blue"><div class="pic" role="img" aria-label="Row of paint brushes dipped in bright colours"></div><div class="label">Painting Services</div></div>
<div class="abs card green"><div class="pic" role="img" aria-label="Squeegee cleaning a soapy window"></div><div class="label">Window Washing</div></div>
<div class="abs card orange"><div class="pic" role="img" aria-label="Chrome sink pipe with a wrench"></div><div class="label">Plumbing</div></div>

<section class="abs testi-head">
  <h2>Testimonials</h2>
  <svg width="30" height="10" viewBox="0 0 30 10"><path d="M8 0 L0 5 L8 10 Z" fill="#aaa"/><path d="M22 0 L30 5 L22 10 Z" fill="#aaa"/></svg>
</section>
<div class="abs testi">
  <div class="bubble"><span class="quote">&ldquo;</span> Sed pharetra, sem in mattis iaculis, lacus erat suscipit orci, a dapibus odio lectus eget tortor. Cras sed facilisis urna. Donec tinci dunt luctus volutpat. Proin at diam tortor. Nulla tincidunt portti tor sodales dolor. <span class="quote">&rdquo;</span></div>
  <svg class="tail" width="44" height="20" viewBox="0 0 44 20"><path d="M0 0 L44 0 L0 20 Z" fill="#fff"/></svg>
  <div class="name">Client Name, City</div>
</div>

<section class="abs faq">
  <div class="badge">
    <svg width="28" height="28" viewBox="0 0 28 28" style="margin-top:10px"><circle cx="14" cy="14" r="13" fill="#e06a2c"/><text x="14" y="20" text-anchor="middle" font-family="Ubuntu,sans-serif" font-weight="700" font-size="17" fill="#fff">?</text></svg>
    <b>FAQs</b>
  </div>
  <h3>Phasellus vitae lorem urna. In pulvinar libero vel enim aliquet rhoncus.</h3>
  <p>Donec interdum, ipsum id sodales tempor, mi turpis molestie arcu, tincidunt placerat ipsum tortor sit amet dolor. Cras auctor velit ves tibulum tellus vehicula varius. Nam tincidunt eros a libero fermentum lacinia. Fusce id lorem in nibh bibendum.</p>
  <svg class="next" width="28" height="28" viewBox="0 0 28 28"><circle cx="14" cy="14" r="13" fill="#e4e4e4"/><path d="M11 8 L17 14 L11 20" fill="none" stroke="#aaa" stroke-width="2.5"/></svg>
</section>

<ul class="abs links" style="left:79px"><li>Integer lobortis</li><li>Curabitur ac</li><li>Phasellus tellus nisl</li><li>Aenean fringilla</li></ul>
<ul class="abs links" style="left:235px"><li>Integer lobortis</li><li>Curabitur ac</li><li>Phasellus tellus nisl</li><li>Aenean fringilla</li></ul>
<ul class="abs links" style="left:391px"><li>Integer lobortis</li><li>Curabitur ac</li><li>Phasellus tellus nisl</li><li>Aenean fringilla</li></ul>
<ul class="abs links" style="left:548px"><li>Integer lobortis</li><li>Curabitur ac</li><li>Phasellus tellus nisl</li><li>Aenean fringilla</li></ul>
<div class="abs col-rule"></div>
<section class="abs signup">
  <h4>Email Signup</h4>
  <div class="field">Email ID</div>
  <div class="submit">SUBMIT</div>
</section>

<footer class="abs footer">
  <p>Copyright &copy; 2013 &nbsp; www.verano.example &nbsp; All rights reserved.</p>
  <div class="social"><span style="background:#2f5aa8"></span><span style="background:#3fa9e0"></span><span style="background:#c4262b"></span></div>
</footer>
</body>
</html>
```